Business card design for Plumbing and Gas fitting company

We need a business card design for our plumbing and gas fitting company using the company logo and director details. Design should be modern and eye-catching however kept reasonably simple. This design should be targeted at commercial businesses/work so professionalism is key.

Target Market(s)

Commercial/business

Industry/Entity Type

Plumbing

Contact Information for Business Card

Warren Dohey
Director
027 581 9043
warren@vantorplumbingandgas.example
PO Box 7816
Palmerston North 4472

Font styles to use
Sans Serif

Requirements
Must have
• Logo
• Modern
• Kept simple
Nice to have
• Colour scheme based around logo

```html
<!DOCTYPE html>
<html lang="en">
<head>
<meta charset="utf-8">
<title>Vantor Plumbing &amp; Gas – Business Card</title>
<link rel="stylesheet" href="https://fonts.googleapis.com/css2?family=Open+Sans:wght@400;600;700&display=swap">
<style>
  :root {
    --page-bg: #e9e9ea;
    --blue-deep: #0b4585;
    --blue-light: #4a8cc6;
    --orange: #e4722c;
    --orange-soft: #efb088;
    --paper-light: #ffffff;
    --paper-shade: #e4e4e6;
    --white: #ffffff;
    --brand-blue: #1565b8;
  }
  html, body {
    margin: 0;
    padding: 0;
    width: 989px;
    height: 1200px;
    overflow: hidden;
    background: var(--page-bg);
  }
  .canvas {
    position: relative;
    width: 989px;
    height: 1200px;
    font-family: "Open Sans", sans-serif;
  }
  .card {
    position: absolute;
    left: 51px;
    width: 878px;
    height: 500px;
    box-shadow: 0 3px 10px rgba(0,0,0,0.18);
  }
  .card--front { top: 51px; }
  .card--back { top: 636px; }
  .card svg { display: block; width: 100%; height: 100%; }
  .stop-blue-a { stop-color: var(--blue-deep); }
  .stop-blue-b { stop-color: var(--blue-light); }
  .stop-paper-a { stop-color: var(--paper-light); }
  .stop-paper-b { stop-color: var(--paper-shade); }
  .stop-orange-a { stop-color: var(--orange); }
  .stop-orange-b { stop-color: var(--orange-soft); }
  .blue-fill { fill: url(#blueFade); }
  .blue-fill-back { fill: url(#blueFadeBack); }
  .accent-fill { fill: url(#orangeFade); }
  .accent-fill-back { fill: url(#orangeFadeBack); }
  .panel { fill: var(--blue-deep); }
  .brand-name {
    font-family: "Open Sans", sans-serif;
    font-weight: 700;
    font-size: 25px;
    fill: var(--brand-blue);
  }
  .brand-dot { fill: var(--orange); }
  .contact-text {
    font-family: "Open Sans", sans-serif;
    font-weight: 600;
    fill: var(--white);
  }
  .contact-email { font-size: 6.6px; }
  .contact-phone { font-size: 10.5px; }
  .contact-post { font-size: 7px; font-weight: 700; }
  .contact-web { font-size: 7px; font-weight: 700; }
  .icon-badge { fill: var(--white); }
  .icon-mark { fill: var(--blue-deep); }
  .icon-line { stroke: var(--blue-deep); fill: none; stroke-width: 1.1; }
  .holder-name {
    font-family: "Open Sans", sans-serif;
    font-weight: 400;
    font-size: 25px;
    fill: var(--white);
  }
  .holder-role {
    font-family: "Open Sans", sans-serif;
    font-weight: 700;
    font-size: 12px;
    letter-spacing: 0.5px;
    fill: var(--white);
  }
</style>
</head>
<body>
<main class="canvas">

  <section class="card card--front" aria-label="Card front">
    <svg viewBox="0 0 631 359" preserveAspectRatio="none">
      <defs>
        <linearGradient id="paperFade" x1="0" y1="0" x2="1" y2="1">
          <stop offset="0" class="stop-paper-a"/>
          <stop offset="1" class="stop-paper-b"/>
        </linearGradient>
        <linearGradient id="blueFade" x1="0" y1="0" x2="1" y2="1">
          <stop offset="0" class="stop-blue-a"/>
          <stop offset="1" class="stop-blue-b"/>
        </linearGradient>
        <linearGradient id="orangeFade" x1="0" y1="0" x2="1" y2="1">
          <stop offset="0" class="stop-orange-a"/>
          <stop offset="1" class="stop-orange-b"/>
        </linearGradient>
      </defs>
      <rect width="631" height="359" fill="url(#paperFade)"/>

      <polygon class="blue-fill" points="0,0 185,0 0,185"/>

      <polygon class="accent-fill" role="img" aria-label="Diagonal orange stripe accent" points="205,0 296,0 0,296 0,205"/>
      <polygon class="accent-fill" role="img" aria-label="Diagonal orange stripe accent" points="631,88 631,160 430,359 360,359"/>

      <polygon class="blue-fill" points="0,359 0,332 118,220 256,359"/>
      <polygon class="blue-fill" points="372,0 631,0 505,134"/>
      <polygon class="blue-fill" role="img" aria-label="Blue corner band with dark stripe accents" points="631,165 435,359 631,359"/>

      <g class="brand-lockup">
        <circle class="brand-dot" cx="186" cy="173" r="9"/>
        <text class="brand-name" x="204" y="182">Vantor Plumbing &amp; Gas</text>
      </g>
    </svg>
  </section>

  <section class="card card--back" aria-label="Card back">
    <svg viewBox="0 0 631 359" preserveAspectRatio="none">
      <defs>
        <linearGradient id="paperFadeBack" x1="0" y1="0" x2="1" y2="1">
          <stop offset="0" class="stop-paper-a"/>
          <stop offset="1" class="stop-paper-b"/>
        </linearGradient>
        <linearGradient id="blueFadeBack" x1="0" y1="1" x2="1" y2="0">
          <stop offset="0" class="stop-blue-a"/>
          <stop offset="1" class="stop-blue-b"/>
        </linearGradient>
        <linearGradient id="orangeFadeBack" x1="1" y1="0" x2="0" y2="1">
          <stop offset="0" class="stop-orange-a"/>
          <stop offset="1" class="stop-orange-b"/>
        </linearGradient>
      </defs>
      <rect width="631" height="359" fill="url(#paperFadeBack)"/>

      <polygon class="blue-fill-back" points="0,0 222,0 105,113 0,8"/>
      <polygon class="blue-fill-back" role="img" aria-label="Blue diagonal band with dark stripe accents" points="600,0 631,0 631,359 268,359"/>

      <polygon class="panel" points="210,110 420,110 236,305 9,305"/>

      <polygon class="accent-fill-back" role="img" aria-label="Diagonal orange stripe accent" points="515,0 593,0 234,359 155,359"/>

      <g class="contact-list">
        <g class="contact-item">
          <circle class="icon-badge" cx="221" cy="128" r="10"/>
          <rect class="icon-mark" x="215" y="124" width="12" height="8" rx="1"/>
          <polyline points="215,124.5 221,129 227,124.5" stroke="#ffffff" stroke-width="1" fill="none"/>
          <text class="contact-text contact-email" x="236" y="130.5">warren@vantorplumbingandgas.example</text>
        </g>
        <g class="contact-item">
          <circle class="icon-badge" cx="176" cy="174" r="10"/>
          <path class="icon-mark" d="M171,168 l3,-1 l2,4 l-2,1.5 q1.5,3.5 4.5,4.5 l1.5,-2 l4,2 l-1,3 q-8,0 -12,-12 z"/>
          <text class="contact-text contact-phone" x="197" y="178">027 581 9043</text>
        </g>
        <g class="contact-item">
          <circle class="icon-badge" cx="124" cy="224" r="10"/>
          <path class="icon-mark" d="M124,231 q-6,-7 -6,-10 a6,6 0 0 1 12,0 q0,3 -6,10 z"/>
          <circle cx="124" cy="221" r="2" fill="#ffffff"/>
          <text class="contact-text contact-post" x="147" y="222">PO Box 7816</text>
          <text class="contact-text contact-post" x="147" y="231">Palmerston North 4472</text>
        </g>
        <g class="contact-item">
          <circle class="icon-badge" cx="80" cy="278" r="10"/>
          <circle class="icon-line" cx="80" cy="278" r="6"/>
          <ellipse class="icon-line" cx="80" cy="278" rx="2.5" ry="6"/>
          <line class="icon-line" x1="74" y1="278" x2="86" y2="278"/>
          <text class="contact-text contact-web" x="99" y="281">YOUR WEBSITE HERE</text>
        </g>
      </g>

      <g class="card-holder">
        <text class="holder-name" x="478" y="242" text-anchor="middle">Warren Dohey</text>
        <text class="holder-role" x="471" y="266" text-anchor="middle">DIRECTOR</text>
      </g>
    </svg>
  </section>

</main>
</body>
</html>
```